Website design for online service business

The company provides the following services:
1 - consultancy services on existing products (like tallydesk and brisk 354)
2 - Coaching services - Coach someone on services like using/developing features with existing products, or teach how to be more productive, or improve their business using automation, etc
3 - Training
- Online training on demand on existing products via vokra (like in Tallydesk and brisk 365)
- Online courses through videos lessons and scripts by offering information products where people will need to register and pay in advance to access the online course. (productivity courses for example)

- The goal is for clients to book time with me for one of those areas without too many clicks.
- Clients will be able to Book time using an integration (it would be good to have the layout integrated with the site.) with this https://planner.brisk-suite.example/owa/calendar/BrightKelpStudio1@brightkelpstudio.bookhub.example/bookings/

- there will be areas for which i whish to build a VIP mailing list. It's referenced on the wireframes

References:
https://www.lanternfieldnotes.example/about/about-dorvan/
https://www.pebblecompass.example/
https://tallydeskguide.example/

Target Market(s)

- Small businesses
- Freelancers

Industry/Entity Type

Business

Number of Pages Required

5+ page

Font styles to use
Sans Serif

Colors

Designer to choose colors to be used in the design.

Requirements
Must have
• Must have the design optimized to the less clicks possible to achieve any action
• The colors of the site should follow the logo (provided in attach)
• It should use other color that belong to the same pallet of colors
• Should contain colors that incentivizes people to click and book something
• Images and backgrounds should be made available
• All images sizes and colors should be provided to be able to develop the site according to the design
Nice to have
• The bookings for the time should be integrated within the design. If not possible a redirection to it can work as well.
Should not have
• Links to social media
• Pop-ups
• Intrusive navigations (like navigation bares on the left or right hand side)
• Should not be a template used by many people

```html
<!DOCTYPE html>
<html lang="en">
<head>
<meta charset="utf-8">
<title>Brightkelp Studio — Consulting, Coaching and Training</title>
<link href="https://fonts.googleapis.com/css2?family=Montserrat:wght@500;600;700&family=Open+Sans:wght@400;600&display=swap" rel="stylesheet">
<style>
:root{
  --blue:#1b6ea8;
  --blue-dark:#145784;
  --orange:#f2a23a;
  --ink:#2c2c2c;
  --muted:#6b6b6b;
  --light:#eeeeee;
  --card:#f2f2f2;
  --dark:#2e2e2e;
  --white:#ffffff;
}
*{margin:0;padding:0;box-sizing:border-box}
html,body{width:1200px;height:3719px;overflow:hidden}
body{position:relative;background:var(--white);font-family:"Open Sans",Arial,sans-serif;color:var(--ink)}
.abs{position:absolute}
h2,h3{font-family:"Montserrat",Arial,sans-serif;color:var(--ink)}
.section-title{position:absolute;left:0;width:1200px;text-align:center;font-size:27px;font-weight:600}
.divider{position:absolute;left:0;width:1200px;display:flex;justify-content:center;align-items:center;gap:10px}
.divider i{display:block;width:40px;height:2px;background:var(--orange)}
.btn{position:absolute;display:flex;align-items:center;justify-content:center;background:var(--blue);color:var(--white);font-family:"Montserrat",Arial,sans-serif;font-size:12px;font-weight:600;text-transform:uppercase;letter-spacing:.5px;text-decoration:none}

/* hero */
.hero{left:0;top:0;width:1200px;height:625px;background:linear-gradient(180deg,#5f6a6e 0%,#8b8a83 40%,#6f7a57 70%,#4d5a3a 100%)}
.brand{position:absolute;top:10px;left:0;width:1200px;display:flex;justify-content:center}
.brand-mark{background:var(--white);padding:14px 28px;display:flex;align-items:center;gap:10px;font-family:"Montserrat",Arial,sans-serif;font-weight:700;font-size:20px;color:var(--blue);text-transform:uppercase;letter-spacing:2px}
.brand-mark span{width:14px;height:14px;border-radius:50%;background:var(--orange)}

/* help cards */
.help-card{position:absolute;top:800px;width:215px;height:288px;background:var(--card);text-align:center;padding:28px 16px 0}
.help-card svg{display:block;margin:0 auto 10px}
.help-card h3{font-size:14px;font-weight:600;margin-bottom:14px}
.help-card p{font-size:10px;line-height:1.6;color:var(--muted)}

/* why */
.why{left:0;top:1183px;width:1200px;height:484px;background:linear-gradient(90deg,#3a3a3a,#262626)}
.why-bg{left:0;top:1183px;width:620px;height:484px;background:linear-gradient(135deg,#4b4f52,#6c6760 60%,#3c3f42)}
.why-frame{left:98px;top:1263px;width:481px;height:334px;border:6px solid var(--orange);box-shadow:6px 6px 0 #2aa0b8;background:linear-gradient(160deg,#8c8f90,#b2a898 55%,#6e6a64)}
.why-title{left:640px;top:1253px;width:480px;text-align:right;color:var(--white);font-size:27px;font-weight:600}
.why-text{left:625px;top:1335px;width:490px;color:var(--white);font-size:11px;line-height:1.75;text-align:right}

/* questions */
.questions{left:0;top:1667px;width:1200px;height:386px;background:var(--light)}
.q-sub{left:0;top:1836px;width:1200px;text-align:center;font-size:11px;color:var(--muted)}
.q-or{position:absolute;top:1916px;font-size:11px;color:var(--muted)}

/* skills */
.skill{position:absolute;top:2228px;width:228px;text-align:center}
.skill-circle{width:228px;height:228px;border-radius:50%;background:#f3f3f3;display:flex;align-items:center;justify-content:center;overflow:hidden}
.skill h3{font-size:15px;font-weight:700;text-transform:uppercase;margin-top:40px}
.skill p{font-size:11px;line-height:1.55;color:var(--muted);margin:6px auto 0;width:170px}
.skill .btn{position:relative;margin:22px auto 0;width:106px;height:30px}

/* video */
.video{left:0;top:2755px;width:1200px;height:298px;background:linear-gradient(180deg,#3b3f55,#5b5470 50%,#463c46)}
.video-title{left:0;top:2814px;width:1200px;text-align:center;color:var(--white);font-size:27px;font-weight:700}

/* contact */
.contact-box{left:98px;top:3293px;width:1004px;height:357px;background:#e4e4e4}
.contact-photo{left:316px;top:3053px;width:510px;height:282px;background:linear-gradient(180deg,#f4f4f4,#d9c2ad 50%,#4a4a4a)}
.contact-title{left:98px;top:3358px;width:1004px;text-align:center;font-size:20px;font-weight:700}
.contact-line{left:98px;width:1004px;text-align:center;font-size:11px;color:var(--muted);line-height:1.6}

.footer{left:0;top:3667px;width:1200px;height:52px;background:#2d2d2d;color:#8a8a8a;font-size:10px;padding:18px 0 0 98px}
</style>
</head>
<body>

<div class="abs hero" role="img" aria-label="Campus building with students on the lawn and a man holding a tablet"></div>
<header class="brand"><div class="brand-mark"><span></span>Brightkelp Studio</div></header>

<h2 class="section-title" style="top:710px">How can i help you with your idea</h2>
<div class="divider" style="top:746px"><i></i>
  <svg width="22" height="16" viewBox="0 0 22 16"><path d="M1 2c4-1 7 0 10 2 3-2 6-3 10-2v12c-4-1-7 0-10 2-3-2-6-3-10-2z" fill="var(--blue)"/><path d="M11 4v12" stroke="#fff" stroke-width="1"/></svg>
<i></i></div>

<article class="help-card" style="left:200px">
  <svg width="30" height="26" viewBox="0 0 30 26"><rect x="2" y="3" width="22" height="15" fill="none" stroke="var(--ink)" stroke-width="2"/><path d="M8 23h10M13 18v5M26 2l-9 11" stroke="var(--ink)" stroke-width="2"/></svg>
  <h3>I Will Teach You</h3>
  <p>I want to learn at my own pace. You teach me how things are done and how it works and I will do it myself.</p>
  <a class="btn" style="left:72px;top:220px;width:72px;height:24px;font-size:9px" href="#">Teach Me</a>
</article>
<article class="help-card" style="left:442px">
  <svg width="30" height="26" viewBox="0 0 30 26"><rect x="3" y="3" width="24" height="16" rx="2" fill="none" stroke="var(--ink)" stroke-width="2"/><path d="M9 19l-3 5 7-5M9 9h12M9 13h8" stroke="var(--ink)" stroke-width="2"/></svg>
  <h3>We Do It Together</h3>
  <p>Lorem ipsum is simply dummy text of the printing and typesetting industry. Lorem ipsum has been the industry's standard dummy text.</p>
  <a class="btn" style="left:72px;top:220px;width:72px;height:24px;font-size:9px" href="#">Let's Do It</a>
</article>
<article class="help-card" style="left:688px">
  <svg width="30" height="26" viewBox="0 0 30 26"><path d="M3 24h24" stroke="var(--ink)" stroke-width="2"/><rect x="5" y="16" width="4" height="8" fill="var(--ink)"/><rect x="12" y="12" width="4" height="12" fill="var(--ink)"/><rect x="19" y="8" width="4" height="16" fill="var(--ink)"/><path d="M4 12L12 5l5 4 8-7M21 2h4v4" fill="none" stroke="var(--ink)" stroke-width="2"/></svg>
  <h3>I'll Do It For You</h3>
  <p>Lorem ipsum is simply dummy text of the printing and typesetting industry. Lorem ipsum has been the industry's standard dummy text.</p>
  <a class="btn" style="left:67px;top:220px;width:82px;height:24px;font-size:9px" href="#">Do It For Me</a>
</article>

<section class="abs why"></section>
<div class="abs why-bg" role="img" aria-label="Man sitting on a railing outside a building"></div>
<div class="abs why-frame" role="img" aria-label="Portrait photo of the consultant"></div>
<h2 class="abs why-title">Why should you hire my services</h2>
<div class="divider" style="top:1297px;left:960px;width:220px"><i></i>
  <svg width="22" height="16" viewBox="0 0 22 16"><path d="M1 2c4-1 7 0 10 2 3-2 6-3 10-2v12c-4-1-7 0-10 2-3-2-6-3-10-2z" fill="var(--blue)"/></svg>
<i></i></div>
<p class="abs why-text">Lorem ipsum dolor sit amet, consectetur adipiscing elit. Quis enim reloquendum? Ita prorsus, inquam; Longum est enim ad omnia respondere, quae a te dicta sunt. Quo ea cognitione facta rei investigatio rerum occultissimarum. Non enim ipsa genuit hominem, sed accepit a natura inchoatum. Duo Reges: constructio interrete. Quis suae urbis conservatorem Codrum, quis Erechthei filias non maxime laudat? Magni enim aestimabat pecuniam non modo non contra leges, sed etiam legibus partam. Dicat pro se ipsa virtus nec dubitabit isti vestro beato M.</p>
<a class="btn" style="left:993px;top:1533px;width:112px;height:28px;font-size:10px" href="#">Read More...</a>

<section class="abs questions"></section>
<h2 class="section-title" style="top:1766px">Do you have any questions?</h2>
<div class="divider" style="top:1802px"><i></i>
  <svg width="22" height="16" viewBox="0 0 22 16"><path d="M1 2c4-1 7 0 10 2 3-2 6-3 10-2v12c-4-1-7 0-10 2-3-2-6-3-10-2z" fill="var(--blue)"/></svg>
<i></i></div>
<p class="abs q-sub">It's ok if you have questions. We haven't worked together or met each other to know do you know it!</p>
<a class="btn" style="left:109px;top:1884px;width:165px;height:81px;font-size:11px;text-transform:none;font-weight:500" href="#">We can work together?</a>
<span class="q-or" style="left:284px">or</span>
<a class="btn" style="left:305px;top:1884px;width:218px;height:81px;font-size:11px;text-transform:none;font-weight:500" href="#">Understand each other</a>
<span class="q-or" style="left:533px">or</span>
<a class="btn" style="left:558px;top:1884px;width:179px;height:81px;font-size:11px;text-transform:none;font-weight:500" href="#">Did I say work together?</a>
<span class="q-or" style="left:760px">Don't</span>
<a class="btn" style="left:828px;top:1884px;width:260px;height:81px;font-size:11px;text-transform:none;font-weight:500" href="#">I have the Experience you are looking for?</a>

<h2 class="section-title" style="top:2128px">What would you like to be bettter at?</h2>
<div class="divider" style="top:2164px"><i></i>
  <svg width="22" height="16" viewBox="0 0 22 16"><path d="M1 2c4-1 7 0 10 2 3-2 6-3 10-2v12c-4-1-7 0-10 2-3-2-6-3-10-2z" fill="var(--blue)"/></svg>
<i></i></div>

<div class="skill" style="left:112px">
  <div class="skill-circle"><span style="font-family:Montserrat,Arial,sans-serif;font-size:26px;font-weight:700;color:var(--blue)">Tallydesk</span></div>
  <h3>Tallydesk</h3>
  <p>Lorem ipsum dolor sit amet, consectetur adipiscing elit. Quis enim reloquendum? Ita prorsus, inquam; Longum est enim ad omnia.</p>
  <a class="btn" href="#">Teach Me</a>
</div>
<div class="skill" style="left:358px">
  <div class="skill-circle"><span style="font-family:Montserrat,Arial,sans-serif;font-size:26px;font-weight:700;color:var(--blue)">Brisk 365</span></div>
  <h3>Brisk 365</h3>
  <p>Lorem ipsum dolor sit amet, consectetur adipiscing elit. Quis enim reloquendum? Ita prorsus, inquam; Longum est enim ad omnia.</p>
  <a class="btn" href="#">Teach Me</a>
</div>
<div class="skill" style="left:610px">
  <div class="skill-circle" role="img" aria-label="Illustration of a laptop with online shopping items" style="background:linear-gradient(160deg,#e9eef2,#9fc1d8 60%,#e8c35a)"></div>
  <h3>Create Online Products</h3>
  <p>Lorem ipsum dolor sit amet, consectetur adipiscing elit. Quis enim reloquendum? Ita prorsus, inquam; Longum est enim ad omnia.</p>
  <a class="btn" href="#">Teach Me</a>
</div>
<div class="skill" style="left:864px">
  <div class="skill-circle" role="img" aria-label="Illustration for a productivity course" style="background:linear-gradient(160deg,#e7c7b9,#f4f4f4 50%,#bfc6cc)"></div>
  <h3>Be More Productive</h3>
  <p>Lorem ipsum dolor sit amet, consectetur adipiscing elit. Quis enim reloquendum? Ita prorsus, inquam; Longum est enim ad omnia.</p>
  <a class="btn" href="#">Teach Me</a>
</div>

<section class="abs video" role="img" aria-label="Audience seated in a lecture hall"></section>
<h2 class="abs video-title">Take a Video Tour to Academic</h2>
<svg class="abs" style="left:548px;top:2875px" width="104" height="104" viewBox="0 0 104 104"><circle cx="52" cy="52" r="49" fill="none" stroke="#fff" stroke-width="4"/><path d="M42 32l30 20-30 20z" fill="#fff"/></svg>

<div class="abs contact-box"></div>
<div class="abs contact-photo" role="img" aria-label="Smiling woman leaning over the panel and pointing down"></div>
<h2 class="abs contact-title">Don't worry about anything</h2>
<p class="abs contact-line" style="top:3396px">I am here for you!</p>
<p class="abs contact-line" style="top:3440px;left:340px;width:520px">Use the below button to book a time slot where we can have a chat about what you need help with and we will take it from there.</p>
<p class="abs contact-line" style="top:3518px">Well coffee included of course!</p>
<a class="btn" style="left:554px;top:3567px;width:92px;height:28px;font-size:10px" href="#">Book Me</a>

<footer class="abs footer">Copyright © Brightkelp Studio 2018</footer>
</body>
</html>
```